Presentation Folder Design Project

We need a folder to be designed, which will be specifically for holding and sharing the different information and collateral to our prospective clients, our partners, and anyone else that would like to learn more about our organization. For this folder you will create and design a 18x12 (When laying open flat), front-to-back as well as inside panels, folder to hold all of our presentation information as well as company collateral. The folder design/shape is going to be very unique. Instead of being a standard folder that opens from right to left, with a fold in the middle of the two halves, this folder will open like two doors in front of the viewer. Essentially, there will be a split down the middle of the front panel with the folds being on both the left and right side of the folder. This will create a left flap and a right flap in the front that will open like French doors and the back of the folder will be one solid panel like a standard folder. On the front flapping ‘doors’ (on the inside of the folder) there will be pockets on the bottom of each flap to hold collateral material like brochures and things of that nature. Additionally, there will be a larger pocket on the bottom of the back panel as well. I would like for there to be a spot where the business card can rest in the middle larger back pocket. It will be centered. This inside panel (or what is essentially the back of the folder after the two front flaps are opened) will also hold different paperwork and company informative material. The overall look I would like to achieve is that the two front flaps are going to be doors opening to the information inside. Kind of like saying “welcome home”, then you open the doors to “walk” inside. Use the 'door' theme in your design.

The folder must demonstrate both attention to detail, sophistication and comfort. Our organization is built around warmth, care and individualized personal attention. The most important aspect of this design is to focus on creating a nurturing, warm, and inviting first impression and feel that would attract a prospective client to want to utilize our services and to feel like they would want to walk through those doors on the front of the folder. They need to want to enter.

I am open to the creativity of the designer to develop something based on the above criteria; however I would like the design to work well with our existing collateral material. What I mean by that is that I want it to look like it is “at home” inside of the folder. Like stylistically it belongs and it fits well with what we have created collateral wide for our other companies.Because of this, I would like for the designer to pull inspiration from the link to our website (Located below) as well as from our recently refreshed business cards, and our 3 company logos (All Attached). This should allow the Folder design to be unique and creative, while still staying inside of a framework and the feel/style that I am looking for.
Updates

There are limited submissions on this design project and I would like to see more. Many more!

Target Market(s)

Seniors(50+), Caring Family Members, Social Workers, Professional or Retired Professional, Affluent, Female

Industry/Entity Type

Business

Requirements
Must have
• • The company logos must be included.

www.harbenhearthteam.example
Nice to have
• I will be contacting individual designers to make adjustments, tweaks, and changes based on a design by design basis. Only designs that demonstrate proximity to my vision will be contacted to make subtle updates to original designs. First impressions are HUGE, both in your designs for me and ultimately my collateral to my clients.

```html
<!DOCTYPE html>
<html lang="en">
<head>
<meta charset="utf-8">
<title>Harben Care Group — Presentation Folder</title>
<link href="https://fonts.googleapis.com/css2?family=Lora:ital,wght@0,400;0,600;1,400&display=swap" rel="stylesheet">
<style>
  :root{
    --bg-deep:#0a2e30;
    --bg-mid:#1f5556;
    --teal:#0b5e60;
    --teal-dark:#094a4c;
    --teal-light:#7fb3b0;
    --pink:#f4938c;
    --white:#ffffff;
    --mat:#ffffff;
  }
  *{box-sizing:border-box;margin:0;padding:0}
  html,body{width:1200px;height:1000px;overflow:hidden}
  body{
    background:radial-gradient(ellipse at 50% 55%,var(--bg-mid) 0%,var(--bg-deep) 75%);
    font-family:"Lora",Georgia,serif;
    position:relative;
  }
  .layout-sheet{
    position:absolute;left:28px;top:295px;width:1144px;height:410px;
    background:var(--mat);
  }
  .panel{position:absolute;top:24px;height:362px;overflow:hidden;background:var(--teal)}
  .panel svg.art{position:absolute;inset:0;width:100%;height:100%}
  .front-doors{left:12px;width:270px}
  .inside-spread{left:302px;width:540px}
  .back-cover{left:862px;width:270px}

  .door-split{position:absolute;left:135px;top:0;width:1px;height:100%;background:var(--teal-dark);opacity:.6}

  .brand{
    position:absolute;color:var(--white);font-weight:400;text-align:center;line-height:1.1;
    display:flex;align-items:center;gap:6px;
  }
  .brand .mark{display:inline-block;width:14px;height:14px;background:var(--white)}
  .front-brand{left:14px;bottom:22px;font-size:13px}
  .front-tagline{
    position:absolute;left:150px;bottom:18px;width:110px;color:var(--white);
    font-style:italic;font-size:9px;line-height:1.35;text-align:center;
  }

  .photo-slot{
    position:absolute;left:135px;top:0;width:270px;height:232px;
    background:linear-gradient(160deg,#c9d98a 0%,#8fb35a 45%,#5f8f4a 100%);
  }
  .photo-tagline{
    position:absolute;left:135px;top:168px;width:270px;text-align:center;
    color:var(--white);font-style:italic;font-size:14px;line-height:1.25;
  }
  .flap-brand{font-size:14px;color:#cfe3e1;flex-direction:column;gap:3px;width:135px}
  .flap-brand .mark{background:#cfe3e1;width:16px;height:16px}
  .flap-brand small{font-size:7px;letter-spacing:2px;text-transform:uppercase}
  .homecare-brand{left:0;top:300px}
  .living-brand{right:0;top:300px}

  .back-logo{position:absolute;left:0;top:66px;width:270px;display:flex;flex-direction:column;align-items:center;color:var(--white)}
  .back-logo .mark{width:84px;height:72px;border-radius:14px;background:var(--pink);margin-bottom:18px}
  .back-logo .name{font-size:30px;line-height:1}
  .back-logo .sub{font-size:8px;letter-spacing:3px;text-transform:uppercase;margin-top:4px;border-top:1px solid var(--white);padding-top:2px}
  .sister-brands{position:absolute;top:232px;left:0;width:270px;display:flex;justify-content:center;gap:28px;color:#cfe3e1;font-size:7px;text-align:center;line-height:1.2}
  .contact{position:absolute;top:290px;left:0;width:270px;text-align:center;color:#cfe3e1;font-size:5.5px;line-height:1.6}
  .web{position:absolute;top:330px;left:0;width:270px;text-align:center;color:var(--white);font-style:italic;font-weight:600;font-size:8px}
</style>
</head>
<body>
<main class="layout-sheet">

  <!-- Front: closed doors -->
  <section class="panel front-doors" aria-label="Front cover, closed doors">
    <svg class="art" viewBox="0 0 270 362" preserveAspectRatio="none">
      <path d="M0,0H270V182Q205,150 135,222Q65,150 0,182Z" fill="var(--teal-light)"/>
      <path d="M0,246Q60,226 120,250Q130,254 135,258V270Q128,264 118,262Q60,242 0,262Z" fill="var(--pink)"/>
      <path d="M270,246Q210,226 150,250Q140,254 135,258V270Q142,264 152,262Q210,242 270,262Z" fill="var(--pink)"/>
      <path d="M0,278Q60,260 120,282Q130,286 135,290V300Q128,296 118,294Q60,276 0,292Z" fill="var(--pink)"/>
      <path d="M270,278Q210,260 150,282Q140,286 135,290V300Q142,296 152,294Q210,276 270,292Z" fill="var(--pink)"/>
    </svg>
    <div class="door-split"></div>
    <div class="brand front-brand"><span class="mark"></span>Harben Care Group</div>
    <p class="front-tagline">Someone you can depend on…<br>Without question.</p>
  </section>

  <!-- Inside: flaps and back panel with pockets -->
  <section class="panel inside-spread" aria-label="Inside spread with pockets">
    <svg class="art" viewBox="0 0 540 362" preserveAspectRatio="none">
      <rect x="0" y="0" width="135" height="362" fill="var(--teal-light)"/>
      <rect x="405" y="0" width="135" height="362" fill="var(--teal-light)"/>
      <path d="M0,196Q70,186 135,222V362H0Z" fill="var(--teal)"/>
      <path d="M0,206Q70,196 135,232V240Q70,206 0,214Z" fill="var(--pink)"/>
      <path d="M0,218Q70,210 135,246V250Q70,220 0,224Z" fill="var(--teal-light)" opacity=".0"/>
      <path d="M540,196Q470,186 405,222V362H540Z" fill="var(--teal)"/>
      <path d="M540,206Q470,196 405,232V240Q470,206 540,214Z" fill="var(--pink)"/>
    </svg>
    <div class="photo-slot" role="img" aria-label="Photo of a smiling caregiver with a senior man in a wheelchair, arms raised outdoors"></div>
    <p class="photo-tagline">Someone you can<br>depend on…<br>Without question.</p>
    <svg class="art" viewBox="0 0 540 362" preserveAspectRatio="none">
      <path d="M135,212Q170,206 205,218Q250,234 270,258Q290,234 335,218Q370,206 405,212V362H135Z" fill="var(--teal)"/>
      <path d="M135,222Q175,214 215,230Q252,246 270,266Q288,246 325,230Q365,214 405,222V230Q365,224 325,240Q288,256 270,274Q252,256 215,240Q175,224 135,230Z" fill="var(--pink)"/>
      <g stroke="var(--teal-dark)" stroke-width="1.2">
        <line x1="232" y1="292" x2="240" y2="300"/><line x1="308" y1="292" x2="300" y2="300"/>
        <line x1="232" y1="340" x2="240" y2="332"/><line x1="308" y1="340" x2="300" y2="332"/>
      </g>
    </svg>
    <div class="brand flap-brand homecare-brand"><span class="mark"></span>Harben<small>Homecare</small></div>
    <div class="brand flap-brand living-brand"><span class="mark"></span>Harben<small>Senior Living</small></div>
  </section>

  <!-- Back cover -->
  <section class="panel back-cover" aria-label="Back cover">
    <div class="back-logo">
      <span class="mark"></span>
      <span class="name">Harben</span>
      <span class="sub">Care Group</span>
    </div>
    <div class="sister-brands">
      <span>Harben<br>Homecare</span>
      <span>Harben<br>Senior Living</span>
    </div>
    <p class="contact">120 Harbor Lane, Suite 4, Hilo, HI 96720<br>Phone: 555-010-2233 • Fax: 555-010-2244<br>Email: info@harbenhomecare.example</p>
    <p class="web">www.harbenhomecare.example</p>
  </section>

</main>
</body>
</html>
```